IT Company that provides secure IT solutions and services to our customers

We need business cards and a logo for a new IT Solutions company just created based in Kuala Lumpur, Malaysia. But will also be serving other countries in the region. We provide secure data, voice solutions on mobile platforms. Our first offering is encrypted voice and data solutions for IOS, Android, Windows and BlackBerry devices.

Target Market(s)

large organizations Govt, Police, Defence, Anti-corruption, Legal, highly regulated industries such as Health-care, Financial, Banking, Insurance,

Industry/Entity Type

Information Technology

Contact Information for Business Card

VornaxIT (Logo - colour is ORBEL blue)Dariush Pelo Managing Director Vornax IT Sdn. Bhd.5th Floor, Block F, Wisma LBD,No.14 Jalan Seri Mewah,50470, Kuala LumpurMalaysia

Font styles to use
Sans Serif

Colors
3176b5
ec1f27
fbed22

Requirements
Must have
• VornaxIT all in Blue like ORBEL blue. A logo design perhaps a play of VI, K with a dangling T (colour can be any)
Nice to have
• I want a clean crisp card, not too busy, easy to read.

```html
<!DOCTYPE html>
<html lang="en">
<head>
<meta charset="utf-8">
<title>Vornax IT – Business Card</title>
<link rel="stylesheet" href="https://fonts.googleapis.com/css2?family=Open+Sans:wght@400;700&display=swap">
<style>
  :root {
    --stage: #000000;
    --card: #ffffff;
    --brand-blue: #1f5fae;
    --brand-red: #d4212a;
    --ink: #1a1a1a;
  }
  * { margin: 0; padding: 0; box-sizing: border-box; }
  html, body {
    width: 1200px;
    height: 900px;
    overflow: hidden;
    background: var(--stage);
    font-family: "Open Sans", Arial, sans-serif;
  }
  .stage {
    position: relative;
    width: 1200px;
    height: 900px;
  }
  .card {
    position: absolute;
    top: 275px;
    width: 477px;
    height: 293px;
    background: var(--card);
  }
  .card--front {
    left: 116px;
    border-radius: 0 60px 0 60px;
  }
  .card--back {
    left: 622px;
    border-radius: 60px 0 60px 0;
  }
  .wordmark {
    position: absolute;
    font-weight: 700;
    color: var(--brand-blue);
    letter-spacing: -1px;
    line-height: 1;
    white-space: nowrap;
  }
  .card--front .wordmark {
    left: 54px;
    top: 104px;
    font-size: 44px;
  }
  .card--back .wordmark {
    left: 92px;
    top: 112px;
    font-size: 48px;
  }
  .holder {
    position: absolute;
    right: 27px;
    top: 34px;
    text-align: right;
  }
  .holder__name {
    font-size: 15px;
    font-weight: 700;
    color: var(--brand-red);
    line-height: 19px;
  }
  .holder__title {
    font-size: 13px;
    color: var(--ink);
    line-height: 18px;
  }
  .company {
    position: absolute;
    right: 27px;
    top: 199px;
    text-align: right;
    font-style: normal;
  }
  .company__name {
    font-size: 15px;
    font-weight: 700;
    color: var(--brand-red);
    line-height: 19px;
  }
  .company__line {
    font-size: 13px;
    color: var(--ink);
    line-height: 17.5px;
    white-space: nowrap;
  }
</style>
</head>
<body>
  <main class="stage">
    <section class="card card--front">
      <div class="wordmark">VornaxIT</div>
      <div class="holder">
        <p class="holder__name">Dariush Pelo</p>
        <p class="holder__title">Managing Director</p>
      </div>
      <address class="company">
        <p class="company__name">Vornax IT</p>
        <p class="company__line">Sdn. Bhd.5th Floor, Block F,&nbsp; Wisma</p>
        <p class="company__line">LBD,No.14 Jalan Seri Mewah, 50470,</p>
        <p class="company__line">Kuala Lumpur Malaysia</p>
      </address>
    </section>
    <section class="card card--back">
      <div class="wordmark">VornaxIT</div>
    </section>
  </main>
</body>
</html>
```